fully distributed
Project: fully distributed
fully distributed  - Information Technology
Creative Brief
Use specific fonts
calibri
Simple
Doug Pelliver
CMO
482 Corwin St , Floor 6 New York NY 10019
doug.pelliver@tulvaro.com
logo only
marcste marcste
on 18 and 19 can you fade the grey a litle so it just looks like a faint color
Xpert Xpert
Sure Sir.
we like some of yr designs can u try the design of 17 with the physical layout of card 2
like what you have started will check each one out
thanks we are looking for stationary too
please add fax number 1 800 937 2584

```html
<!DOCTYPE html>
<html lang="en">
<head>
<meta charset="utf-8">
<title>Tulvaro stationery</title>
<link href="https://fonts.googleapis.com/css2?family=Carlito:wght@400;700&display=swap" rel="stylesheet">
<style>
  :root{
    --red:#e8323c;
    --ink:#1d1d1d;
    --grey:#6b6b6b;
    --line:#c9c9c9;
    --paper:#ffffff;
    --stage:#dcdcdc;
  }
  *{box-sizing:border-box;margin:0;padding:0}
  html,body{width:1200px;height:961px;overflow:hidden}
  body{background:var(--stage);font-family:"Carlito",Calibri,Arial,sans-serif;color:var(--ink);position:relative}
  .piece{position:absolute;background:var(--paper);overflow:hidden}
  .brand{display:flex;align-items:center;gap:.18em;font-weight:700;color:var(--ink);line-height:1;letter-spacing:-.01em;white-space:nowrap}
  .brand-dot{width:.32em;height:.32em;border-radius:50%;background:var(--red);display:inline-block}
  .tagline{color:var(--red);font-weight:700;line-height:1;white-space:nowrap}
  .bar{position:absolute;height:4px}
  .bar.black{background:var(--ink)}
  .bar.red{background:var(--red)}

  /* letterhead */
  .letter-backing{position:absolute;left:151px;top:78px;width:469px;height:625px;background:var(--red)}
  .letterhead{left:120px;top:44px;width:463px;height:648px}
  .letterhead .brand{position:absolute;left:18px;top:16px;font-size:40px}
  .letterhead .tagline{position:absolute;left:20px;top:58px;font-size:10.5px}
  .contact{position:absolute;font-size:8.5px;line-height:1.45;color:var(--grey);white-space:nowrap}
  .letterhead .contact{left:330px;top:14px}
  .contact .row{display:flex;align-items:center;gap:5px}
  .contact .ico{width:9px;height:9px;flex:none}
  .letter-body{position:absolute;left:32px;top:185px;width:400px;font-size:9px;line-height:2.1;color:#444}
  .letter-body p+p{margin-top:10px}
  .signature{position:absolute;right:60px;top:505px}
  .signature .name{color:var(--red);font-size:21px}
  .signature .title{font-size:10px;color:var(--ink);margin-left:40px}

  /* envelope */
  .envelope{left:690px;top:117px;width:393px;height:208px}
  .envelope .flap{position:absolute;left:0;top:0;width:393px;height:96px}
  .envelope .brand{position:absolute;left:148px;top:14px;font-size:30px;color:#fff}
  .envelope .brand-dot{background:#fff}
  .envelope .tagline{position:absolute;left:0;right:0;top:44px;text-align:center;font-size:8px;color:#fff}
  .envelope .contact{left:14px;top:112px;font-size:7px}
  .envelope .contact .ico{width:7px;height:7px}
  .envelope .rules{position:absolute;left:225px;top:132px;width:150px}
  .envelope .rules span{display:block;border-bottom:1px solid var(--line);height:15px}

  /* cards */
  .card{width:206px;height:122px}
  .card-contact{left:760px;top:396px}
  .card-front{left:760px;top:560px}
  .card-wide-contact{left:182px;top:763px;width:232px;height:138px}
  .card-wide-front{left:448px;top:763px;width:234px;height:138px}
  .card-contact .brand{position:absolute;left:12px;top:44px;font-size:19px}
  .card-contact .tagline{position:absolute;left:13px;top:64px;font-size:5.2px}
  .card-contact .who{position:absolute;left:118px;top:20px;font-size:6px;color:var(--grey);line-height:1.45;white-space:nowrap}
  .who .name{color:var(--red);font-size:10.5px;line-height:1.2}
  .card-front .brand,.card-wide-front .brand{position:absolute;left:50%;transform:translateX(-50%)}
  .card-front .brand{top:40px;font-size:26px}
  .card-front .tagline{position:absolute;left:0;right:0;top:70px;text-align:center;font-size:6.5px}
  .card-wide-front .brand{top:44px;font-size:29px}
  .card-wide-front .tagline{position:absolute;left:0;right:0;top:78px;text-align:center;font-size:7px}
  .card-wide-contact .brand{position:absolute;left:14px;top:18px;font-size:27px}
  .card-wide-contact .tagline{position:absolute;left:15px;top:48px;font-size:6.5px}
  .card-wide-contact .who{position:absolute;left:15px;top:66px;font-size:6.5px;color:var(--grey);line-height:1.45;white-space:nowrap}
  .edge{position:absolute;background:var(--red)}
</style>
</head>
<body>

<svg width="0" height="0" style="position:absolute" aria-hidden="true">
  <defs>
    <symbol id="ico-phone" viewBox="0 0 10 10"><circle cx="5" cy="5" r="5" fill="#e8323c"/><path d="M3.3 2.6l1 .9-.5.8c.3.6.8 1.1 1.4 1.4l.8-.5.9 1-.6.9C4.6 7 3 5.4 2.9 3.2z" fill="#fff"/></symbol>
    <symbol id="ico-fax" viewBox="0 0 10 10"><circle cx="5" cy="5" r="5" fill="#e8323c"/><rect x="2.6" y="4" width="4.8" height="2.6" fill="#fff"/><rect x="3.4" y="2.4" width="3.2" height="1.4" fill="#fff"/></symbol>
    <symbol id="ico-mail" viewBox="0 0 10 10"><circle cx="5" cy="5" r="5" fill="#e8323c"/><rect x="2.5" y="3.2" width="5" height="3.6" fill="#fff"/><path d="M2.5 3.2L5 5.3l2.5-2.1" stroke="#e8323c" stroke-width=".6" fill="none"/></symbol>
  </defs>
</svg>

<!-- Letterhead -->
<div class="letter-backing"></div>
<section class="piece letterhead">
  <div class="brand">tulvaro<span class="brand-dot"></span></div>
  <div class="tagline">Networks Built to Reach Everywhere</div>
  <div class="contact">
    <div>482 Corwin St , Floor 6</div>
    <div>New York NY 10019</div>
    <div class="row" style="margin-top:8px"><svg class="ico"><use href="#ico-phone"/></svg>+1 212 555 0173</div>
    <div class="row"><svg class="ico"><use href="#ico-fax"/></svg>1 800 937 2584</div>
    <div class="row"><svg class="ico"><use href="#ico-mail"/></svg>doug.pelliver@tulvaro.com</div>
  </div>
  <div class="letter-body">
    <p>Our team builds distributed systems that keep every office, device and person connected with the tools they rely on each day. We plan, deploy and support networks across many sites, so your staff can work from anywhere without delay or worry. Each project starts with a clear review of your needs and ends with a system that grows with you.</p>
    <p>Our engineers stay with you after launch, watching performance, applying updates and answering questions quickly, so small issues never turn into long outages for your business or your clients.</p>
    <p>Thank you for your time and trust. We look forward to working with you on the next stage of your plans and to hearing from you soon.</p>
  </div>
  <div class="signature">
    <div class="name">Doug Pelliver</div>
    <div class="title">CMO</div>
  </div>
  <span class="bar black" style="left:222px;bottom:0;width:34px"></span>
  <span class="bar red" style="left:256px;bottom:0;width:20px"></span>
  <span class="bar black" style="right:22px;bottom:0;width:30px"></span>
  <span class="bar red" style="right:0;bottom:0;width:22px"></span>
</section>

<!-- Envelope -->
<section class="piece envelope">
  <svg class="flap" viewBox="0 0 393 96" preserveAspectRatio="none" aria-hidden="true">
    <path d="M0 0H393V28Q300 60 196 96Q92 60 0 28Z" fill="#e8323c"/>
  </svg>
  <div class="brand">tulvaro<span class="brand-dot"></span></div>
  <div class="tagline">Networks Built to Reach Everywhere</div>
  <div class="contact">
    <div>482 Corwin St , Floor 6</div>
    <div>New York NY 10019</div>
    <div class="row" style="margin-top:5px"><svg class="ico"><use href="#ico-phone"/></svg>+1 212 555 0173</div>
    <div class="row"><svg class="ico"><use href="#ico-fax"/></svg>1 800 937 2584</div>
    <div class="row"><svg class="ico"><use href="#ico-mail"/></svg>doug.pelliver@tulvaro.com</div>
  </div>
  <div class="rules"><span></span><span></span><span></span><span></span></div>
  <span class="bar black" style="left:0;bottom:0;width:24px"></span>
  <span class="bar red" style="left:24px;bottom:0;width:14px"></span>
  <span class="bar black" style="right:14px;bottom:0;width:24px"></span>
  <span class="bar red" style="right:0;bottom:0;width:14px"></span>
</section>

<!-- Business card, contact side -->
<section class="piece card card-contact">
  <span class="edge" style="left:0;top:0;width:206px;height:4px"></span>
  <span class="edge" style="left:0;top:0;width:4px;height:34px"></span>
  <div class="brand">tulvaro<span class="brand-dot"></span></div>
  <div class="tagline">Networks Built to Reach Everywhere</div>
  <div class="who">
    <div class="name">Doug Pelliver</div>
    <div style="margin-bottom:6px">CMO</div>
    <div>482 Corwin St , Floor 6</div>
    <div>New York NY 10019</div>
    <div style="margin-top:4px">+1 212 555 0173</div>
    <div>1 800 937 2584</div>
    <div>doug.pelliver@tulvaro.com</div>
  </div>
  <span class="bar black" style="right:14px;bottom:0;width:16px;height:3px"></span>
  <span class="bar red" style="right:0;bottom:0;width:14px;height:3px"></span>
</section>

<!-- Business card, logo side -->
<section class="piece card card-front">
  <span class="edge" style="left:0;top:0;width:60px;height:4px"></span>
  <span class="edge" style="left:0;top:0;width:4px;height:30px"></span>
  <div class="brand">tulvaro<span class="brand-dot"></span></div>
  <div class="tagline">Networks Built to Reach Everywhere</div>
  <span class="edge" style="right:0;bottom:0;width:60px;height:4px"></span>
  <span class="edge" style="right:0;bottom:0;width:4px;height:30px"></span>
</section>

<!-- Wide card, contact side -->
<section class="piece card-wide-contact">
  <span class="edge" style="left:0;top:0;width:232px;height:4px"></span>
  <div class="brand">tulvaro<span class="brand-dot"></span></div>
  <div class="tagline">Networks Built to Reach Everywhere</div>
  <div class="who">
    <div class="name">Doug Pelliver</div>
    <div style="margin-bottom:3px">CMO</div>
    <div>482 Corwin St , Floor 6 New York NY 10019</div>
    <div>+1 212 555 0173 · 1 800 937 2584</div>
    <div>doug.pelliver@tulvaro.com</div>
  </div>
  <span class="bar black" style="left:0;bottom:0;width:22px"></span>
  <span class="bar red" style="left:22px;bottom:0;width:14px"></span>
</section>

<!-- Wide card, logo side -->
<section class="piece card-wide-front">
  <div class="brand">tulvaro<span class="brand-dot"></span></div>
  <div class="tagline">Networks Built to Reach Everywhere</div>
  <span class="bar black" style="left:0;top:0;width:22px"></span>
  <span class="bar red" style="left:22px;top:0;width:14px"></span>
  <span class="bar black" style="right:14px;bottom:0;width:22px"></span>
  <span class="bar red" style="right:0;bottom:0;width:14px"></span>
</section>

</body>
</html>
```